Start a weight loss Clinic

build a landing page website using the content from this websites. we want to copy all the content from slimpathcoaching.net but make page look more professional. we dont have a logo yet but url is www.brightvitalitycentre.com
https://clinicwellnessalliancegroup.net/home-page
https://www.slimpathcoaching.net/

Target Market(s)

people looking to open a weightloss clinic or a franchise opportunity

Coding

Number of Pages Required

3 page

Requirements
Must have
• copy all content from other site https://www.slimpathcoaching.net/

```html
<!DOCTYPE html>
<html lang="en">
<head>
<meta charset="utf-8">
<title>Bright Vitality Centre</title>
<link href="https://fonts.googleapis.com/css2?family=Roboto:wght@400;500;700&display=swap" rel="stylesheet">
<style>
:root{
  --red:#d42a2f;
  --red-dark:#b81f25;
  --blue:#1b4a8c;
  --blue-dark:#143a70;
  --ink:#222;
  --muted:#666;
  --white:#fff;
}
*{margin:0;padding:0;box-sizing:border-box}
html,body{width:1200px;height:3980px;overflow:hidden;background:var(--white)}
body{font-family:"Roboto",Arial,sans-serif;color:var(--ink);position:relative}
.abs{position:absolute}
.backdrop{position:absolute;left:0;top:0}
.topline{left:0;top:0;width:1200px;height:4px;background:var(--blue)}
.brand{left:109px;top:30px;font-size:22px;font-weight:700;color:var(--ink)}
.nav a{position:absolute;top:35px;font-size:15px;color:#444;text-decoration:none}
.btn{position:absolute;display:flex;align-items:center;justify-content:center;gap:10px;font-size:16px;font-weight:700;text-decoration:none}
.btn .dot{width:17px;height:17px;border-radius:50%;display:inline-flex;align-items:center;justify-content:center}
.btn-red{background:var(--red);color:var(--white)}
.btn-red .dot{background:var(--white)}
.btn-red .dot svg path{stroke:var(--red)}
.btn-blue{background:var(--blue);color:var(--white)}
.btn-blue .dot{background:var(--white)}
.btn-blue .dot svg path{stroke:var(--blue)}
.btn-white{background:var(--white);color:var(--red)}
.btn-white .dot{background:var(--red)}
.btn-white .dot svg path{stroke:var(--white)}
.hero-title{left:110px;top:178px;font-size:72px;line-height:81px;font-weight:700;color:var(--white)}
.hero-photo{left:640px;top:140px;width:470px;height:585px;border-radius:46% 40% 36% 44%;background:radial-gradient(circle at 45% 35%,#b8b4ae,#7f8c8f 55%,#3e6068 100%)}
.section-title{font-size:42px;font-weight:700;color:var(--ink);text-align:center;width:1200px;left:0}
.intro-text{left:170px;width:860px;top:950px;text-align:center;font-size:15px;line-height:26px;color:var(--muted)}
.about-block{left:0;top:1201px;width:467px;height:601px;background:var(--blue);border-top-right-radius:70px}
.about-photo{left:70px;top:1283px;width:528px;height:437px;background:linear-gradient(135deg,#a9b76a 0%,#d9d2c4 40%,#6a2440 70%,#c8c3bb 100%)}
.about-title{left:668px;top:1278px;font-size:42px;font-weight:700}
.about-text{left:668px;top:1347px;width:420px;font-size:14.5px;line-height:26.5px;color:var(--muted)}
.offer-title{color:var(--white);top:1870px}
.card{position:absolute;top:1965px;width:232px;height:231px;background:var(--white);box-shadow:0 4px 14px rgba(0,0,0,.12);text-align:center}
.card .icon{width:96px;height:96px;margin:32px auto 0;border-radius:10px}
.card p{margin-top:28px;font-size:14.5px;line-height:23px;font-weight:500;color:var(--ink)}
.label{position:absolute;font-size:17px;font-weight:500;line-height:25px;color:#333;text-transform:uppercase}
.label.r{text-align:right}
.badges{left:132px;top:3350px;width:935px;height:154px;background:var(--white);box-shadow:0 4px 18px rgba(0,0,0,.15)}
.footer-h{font-size:26px;font-weight:500;color:var(--white)}
.footer-t{font-size:15px;color:var(--white);line-height:27px}
.contact-box{left:728px;top:3550px;width:360px;height:380px;background:var(--red)}
.contact-head{left:742px;top:3563px;width:333px;height:59px;background:var(--white);font-size:26px;font-weight:500;display:flex;align-items:center;justify-content:center;color:var(--ink)}
.field{position:absolute;left:750px;width:317px;border-bottom:1px solid rgba(255,255,255,.8);font-size:15px;color:var(--white);padding-bottom:14px}
.copy{left:111px;top:3920px;font-size:11px;color:var(--white)}
</style>
</head>
<body>

<svg class="backdrop" width="1200" height="3980" viewBox="0 0 1200 3980">
  <defs>
    <linearGradient id="heroRed" x1="0" y1="0" x2="1" y2="1">
      <stop offset="0" stop-color="#d8343a"/><stop offset="1" stop-color="#c7242a"/>
    </linearGradient>
    <linearGradient id="footBlue" x1="0" y1="0" x2="0" y2="1">
      <stop offset="0" stop-color="#1f559c"/><stop offset="1" stop-color="#163f7a"/>
    </linearGradient>
  </defs>
  <path d="M0 84 H1200 V420 C1000 480 760 700 460 716 C260 728 100 680 0 600 Z" fill="url(#heroRed)"/>
  <path d="M0 1802 H1200 V2150 C1000 2230 860 2420 620 2436 C360 2450 150 2400 0 2320 Z" fill="url(#heroRed)"/>
  <path d="M0 3690 C300 3640 520 3480 800 3440 C980 3420 1100 3420 1200 3430 V3980 H0 Z" fill="url(#footBlue)"/>
</svg>

<div class="abs topline"></div>
<div class="abs brand">Bright Vitality Centre</div>
<nav class="nav">
  <a style="left:461px">Home</a>
  <a style="left:537px">About Us</a>
  <a style="left:634px">What We Offer</a>
  <a style="left:768px">Compare</a>
  <a style="left:864px">FAQ</a>
</nav>
<a class="btn btn-blue" style="left:931px;top:22px;width:157px;height:46px">Contact Us <span class="dot"><svg width="9" height="9" viewBox="0 0 9 9"><path d="M3 1.5 L6 4.5 L3 7.5" fill="none" stroke-width="1.8"/></svg></span></a>

<h1 class="abs hero-title">WELCOME TO<br>BRIGHT<br>VITALITY<br>CENTRE</h1>
<a class="btn btn-white" style="left:110px;top:540px;width:158px;height:46px">Get Started <span class="dot"><svg width="9" height="9" viewBox="0 0 9 9"><path d="M3 1.5 L6 4.5 L3 7.5" fill="none" stroke-width="1.8"/></svg></span></a>
<div class="abs hero-photo" role="img" aria-label="Photo of a tired man in workout clothes sitting on an exercise ball"></div>

<h2 class="abs section-title" style="top:826px;line-height:52px">START YOUR OWN PROFITABLE WEIGHT<br>LOSS CLINIC!</h2>
<p class="abs intro-text">We are not a weight loss franchise – you are simply buying our business model, training and support for one low fee. Please<br>read about us, look at what we offer and compare us to weight loss franchises in the marketplace.<br>We offer you a free market analysis and sample break even analysis for your area. We think you will be happy you found us!</p>
<a class="btn btn-red" style="left:522px;top:1056px;width:156px;height:46px">Read More <span class="dot"><svg width="9" height="9" viewBox="0 0 9 9"><path d="M3 1.5 L6 4.5 L3 7.5" fill="none" stroke-width="1.8"/></svg></span></a>

<div class="abs about-block"></div>
<div class="abs about-photo" role="img" aria-label="Photo of a woman doing crunches on a yoga mat at home"></div>
<h2 class="abs about-title">ABOUT US</h2>
<div class="abs about-text">
  <p>Bright Vitality Centre now offers our model to you so you can add weight loss and wellness programs to your existing medical practice or open a stand alone weight loss and wellness center.</p>
  <p>We are not a weight loss franchise – you are simply buying our business model, training and support for one low fee. Please read about us, look at what we offer and compare us to weight loss franchises in the marketplace.</p>
  <p style="margin-top:26px">We now offer you a free market analysis and sample break even analysis for your area. Please see our contact page.</p>
</div>
<a class="btn btn-red" style="left:668px;top:1669px;width:157px;height:46px">Read More <span class="dot"><svg width="9" height="9" viewBox="0 0 9 9"><path d="M3 1.5 L6 4.5 L3 7.5" fill="none" stroke-width="1.8"/></svg></span></a>

<h2 class="abs section-title offer-title">WHAT WE OFFER</h2>
<div class="card" style="left:111px"><div class="icon" role="img" aria-label="Rising bar chart icon" style="background:linear-gradient(135deg,#fbe3d6,#f6c1a6)"></div><p>One-on-one Business &amp;<br>Medical Training</p></div>
<div class="card" style="left:360px"><div class="icon" role="img" aria-label="Social media marketing icon" style="background:linear-gradient(135deg,#dcecfb,#ffe6a8)"></div><p>Marketing &amp; Advertising<br>Training</p></div>
<div class="card" style="left:608px"><div class="icon" role="img" aria-label="Clipboard with programs icon" style="background:linear-gradient(135deg,#ffe9b8,#d6ecf7)"></div><p>Diets, Patient Protocols &amp;<br>Programs</p></div>
<div class="card" style="left:856px"><div class="icon" role="img" aria-label="Open manual book icon" style="background:linear-gradient(135deg,#eef1f3,#cfeee6)"></div><p>Office &amp; Operations<br>Manuals</p></div>
<a class="btn btn-white" style="left:522px;top:2250px;width:156px;height:46px">Get Started <span class="dot"><svg width="9" height="9" viewBox="0 0 9 9"><path d="M3 1.5 L6 4.5 L3 7.5" fill="none" stroke-width="1.8"/></svg></span></a>

<h2 class="abs section-title" style="top:2510px">COMPARE</h2>
<svg class="abs" style="left:0;top:2540px" width="1200" height="540" viewBox="0 2540 1200 540">
  <circle cx="610" cy="2770" r="148" fill="#fff" stroke="var(--blue)" stroke-width="11"/>
  <text x="610" y="2730" text-anchor="middle" font-family="Roboto,sans-serif" font-size="44" font-weight="500" fill="var(--red)">Bright</text>
  <text x="610" y="2785" text-anchor="middle" font-family="Roboto,sans-serif" font-size="44" font-weight="500" fill="var(--red)">Vitality</text>
  <text x="610" y="2840" text-anchor="middle" font-family="Roboto,sans-serif" font-size="44" font-weight="500" fill="var(--red)">Centre</text>
  <g fill="none" stroke="#777" stroke-width="2">
    <g transform="translate(355 2703)"><g transform="rotate(15)"><polygon points="38,-38 84,0 38,38" fill="var(--red)" stroke="none"/><circle r="58" fill="var(--red)" stroke="none"/><circle r="47" fill="#fff" stroke="none"/></g><circle r="18"/><path d="M-18 0 H18 M0 -18 V18"/></g>
    <g transform="translate(355 2837)"><g transform="rotate(-15)"><polygon points="38,-38 84,0 38,38" fill="var(--blue)" stroke="none"/><circle r="58" fill="var(--blue)" stroke="none"/><circle r="47" fill="#fff" stroke="none"/></g><path d="M-20 10 L-22 -12 L-10 0 L0 -16 L10 0 L22 -12 L20 10 Z"/></g>
    <g transform="translate(425 2943)"><g transform="rotate(-43)"><polygon points="38,-38 84,0 38,38" fill="var(--red)" stroke="none"/><circle r="58" fill="var(--red)" stroke="none"/><circle r="47" fill="#fff" stroke="none"/></g><circle cy="-8" r="12"/><path d="M-18 14 L-6 4 L6 14 L18 4"/></g>
    <g transform="translate(540 3027)"><g transform="rotate(-75)"><polygon points="38,-38 84,0 38,38" fill="var(--blue)" stroke="none"/><circle r="58" fill="var(--blue)" stroke="none"/><circle r="47" fill="#fff" stroke="none"/></g><circle r="10"/><path d="M-20 0 H-12 M12 0 H20 M0 -20 V-12 M0 12 V20"/></g>
    <g transform="translate(680 3027)"><g transform="rotate(-105)"><polygon points="38,-38 84,0 38,38" fill="var(--red)" stroke="none"/><circle r="58" fill="var(--red)" stroke="none"/><circle r="47" fill="#fff" stroke="none"/></g><rect x="-18" y="-14" width="24" height="28"/><rect x="10" y="-14" width="10" height="10"/></g>
    <g transform="translate(797 2953)"><g transform="rotate(-136)"><polygon points="38,-38 84,0 38,38" fill="var(--blue)" stroke="none"/><circle r="58" fill="var(--blue)" stroke="none"/><circle r="47" fill="#fff" stroke="none"/></g><rect x="-16" y="-20" width="32" height="36"/><path d="M-9 -8 H9 M-9 0 H9 M-9 8 H3"/></g>
    <g transform="translate(866 2837)"><g transform="rotate(-165)"><polygon points="38,-38 84,0 38,38" fill="var(--red)" stroke="none"/><circle r="58" fill="var(--red)" stroke="none"/><circle r="47" fill="#fff" stroke="none"/></g><path d="M-18 -10 L-4 -18 L16 -8 L18 10 L2 18 L-16 8 Z"/></g>
    <g transform="translate(866 2703)"><g transform="rotate(165)"><polygon points="38,-38 84,0 38,38" fill="var(--blue)" stroke="none"/><circle r="58" fill="var(--blue)" stroke="none"/><circle r="47" fill="#fff" stroke="none"/></g><circle r="19"/><circle cy="-4" r="6"/></g>
  </g>
</svg>
<div class="label r" style="left:68px;width:200px;top:2677px">No Mandatory<br>Vendors</div>
<div class="label r" style="left:60px;width:200px;top:2829px">No % Royalties</div>
<div class="label r" style="left:97px;width:240px;top:2972px">No Convention Fees</div>
<div class="label r" style="left:236px;width:240px;top:3077px">No Scope of Practice<br>Limits</div>
<div class="label" style="left:729px;top:3077px">No % Advertising<br>Fees</div>
<div class="label" style="left:890px;top:2954px">No Monthly<br>Licensing Fees</div>
<div class="label" style="left:950px;top:2817px">No Territory<br>Fees</div>
<div class="label" style="left:950px;top:2677px">No Franchise<br>Fees</div>
<a class="btn btn-red" style="left:504px;top:3196px;width:193px;height:46px">Compare Now <span class="dot"><svg width="9" height="9" viewBox="0 0 9 9"><path d="M3 1.5 L6 4.5 L3 7.5" fill="none" stroke-width="1.8"/></svg></span></a>

<div class="abs badges"></div>
<div class="abs" role="img" aria-label="Accreditation badge" style="left:189px;top:3377px;width:76px;height:76px;border-radius:50%;background:#2c6ea8"></div>
<div class="abs" role="img" aria-label="Professional society membership badge" style="left:495px;top:3382px;width:68px;height:68px;border-radius:50%;background:#6b3b78"></div>
<div class="abs" role="img" aria-label="Medical academy membership badge" style="left:888px;top:3380px;width:124px;height:80px;background:#24426f"></div>

<div class="abs contact-box"></div>
<div class="abs contact-head">CONTACT US</div>
<div class="field" style="top:3660px">Full Name</div>
<div class="field" style="top:3726px">Contact Number</div>
<div class="field" style="top:3792px">Email Address</div>
<div class="field" style="top:3858px">Messgae....</div>
<svg class="abs" style="left:1046px;top:3860px" width="20" height="20" viewBox="0 0 20 20"><path d="M1 9 L19 1 L12 19 L9 11 Z" fill="#fff"/></svg>

<div class="abs footer-h" style="left:111px;top:3718px">GET IN TOUCH</div>
<svg class="abs" style="left:111px;top:3772px" width="18" height="20" viewBox="0 0 18 20"><path d="M9 1 C4.5 1 2 4 2 7.5 C2 12 9 19 9 19 C9 19 16 12 16 7.5 C16 4 13.5 1 9 1 Z" fill="none" stroke="#fff" stroke-width="2"/><circle cx="9" cy="7.5" r="2.5" fill="#fff"/></svg>
<div class="abs footer-t" style="left:152px;top:3770px">4410 Maple Ridge Road<br>Suite 210, Brookfield, GA 30099</div>
<svg class="abs" style="left:111px;top:3834px" width="18" height="18" viewBox="0 0 18 18"><path d="M3 1 L7 1 L8 5 L6 7 C7 10 8 11 11 12 L13 10 L17 11 L17 15 C17 16 16 17 15 17 C7 17 1 11 1 3 C1 2 2 1 3 1 Z" fill="#fff"/></svg>
<div class="abs footer-t" style="left:152px;top:3830px">(877) 555-0142</div>
<svg class="abs" style="left:111px;top:3864px" width="18" height="14" viewBox="0 0 18 14"><rect x="1" y="1" width="16" height="12" fill="none" stroke="#fff" stroke-width="1.6"/><path d="M1 1 L9 8 L17 1" fill="none" stroke="#fff" stroke-width="1.6"/></svg>
<div class="abs footer-t" style="left:152px;top:3857px">hello@brightvitalitycentre.com</div>

<div class="abs footer-h" style="left:460px;top:3718px">QUICK LINKS</div>
<div class="abs footer-t" style="left:460px;top:3770px">Home<br>About Us<br>What We Offer<br>Compare</div>
<div class="abs footer-t" style="left:614px;top:3770px">Faq<br>Contact</div>

<div class="abs copy">© Copyright 2023 Bright Vitality Centre | All Rights Reserved.</div>
</body>
</html>
```